Business card and stationary for tattoo photography company
Velvet Harbor Photography
Business card and stationary for tattoo photography company - Photography
Creative Brief
Modern
Rolf Lindqvist
Photographer / Owner
4630 Marlow Ave W Parrish, FL 34218
rolf@velvetharborphotoworks.com
www.velvetharborphotoworks.com
Strength, Elegance, and Beauty

```html
<!DOCTYPE html>
<html lang="en">
<head>
<meta charset="UTF-8">
<title>Velvet Harbor Photography – Business Card</title>
<link href="https://fonts.googleapis.com/css2?family=Tinos:wght@400;700&display=swap" rel="stylesheet">
<style>
  :root {
    --backdrop: #e9e9e9;
    --card-white: #ffffff;
    --card-black: #0c0c0c;
    --ink: #2a2a2a;
    --ink-soft: #6b6b6b;
    --accent-red: #c8182a;
    --photo-light: #9a9a9a;
    --photo-mid: #4a4a4a;
    --photo-dark: #141414;
    --ornament: #ececec;
  }
  * { margin: 0; padding: 0; box-sizing: border-box; }
  html, body { width: 1200px; height: 674px; overflow: hidden; }
  body {
    background: var(--backdrop);
    font-family: "Tinos", "Times New Roman", serif;
    display: flex;
    align-items: center;
    justify-content: center;
    gap: 50px;
  }
  .card {
    position: relative;
    width: 525px;
    height: 300px;
    overflow: hidden;
    box-shadow: 0 6px 18px rgba(0,0,0,0.18);
  }

  /* Front side */
  .card-front { background: var(--card-black); }
  .card-front .photo {
    position: absolute;
    inset: 0;
    background:
      radial-gradient(ellipse 45% 60% at 58% 50%, var(--photo-light) 0%, var(--photo-mid) 45%, transparent 80%),
      linear-gradient(90deg, var(--photo-dark) 0%, var(--photo-mid) 55%, var(--photo-dark) 100%);
  }
  .card-front .brand-block {
    position: absolute;
    left: 28px;
    bottom: 34px;
    color: #ffffff;
  }
  .card-front .brand-name {
    font-size: 30px;
    font-weight: 400;
    color: #ffffff;
    line-height: 1;
  }
  .card-front .tagline {
    margin-top: 8px;
    font-size: 12px;
    letter-spacing: 0.5px;
    color: #dcdcdc;
  }

  /* Back side */
  .card-back { background: var(--card-white); }
  .card-back .ornament {
    position: absolute;
    right: 20px;
    bottom: 12px;
    width: 150px;
    height: 80px;
    border-radius: 50%;
    background: radial-gradient(ellipse at center, var(--ornament) 0%, transparent 70%);
  }
  .contact-block {
    position: absolute;
    left: 40px;
    top: 72px;
  }
  .person-name {
    font-size: 17px;
    font-weight: 700;
    color: var(--ink);
  }
  .person-title {
    margin-top: 2px;
    font-size: 8.5px;
    letter-spacing: 1.2px;
    text-transform: uppercase;
    color: var(--ink-soft);
  }
  .contact-list {
    list-style: none;
    margin-top: 14px;
  }
  .contact-list li {
    display: flex;
    align-items: baseline;
    font-size: 10.5px;
    line-height: 17px;
    color: var(--ink);
  }
  .contact-list .label {
    width: 16px;
    font-weight: 700;
    font-size: 9px;
    color: var(--accent-red);
  }
  .card-back .brand-name {
    position: absolute;
    right: 36px;
    top: 120px;
    font-size: 28px;
    font-weight: 400;
    color: var(--ink);
    line-height: 1;
  }
</style>
</head>
<body>
  <section class="card card-front">
    <div class="photo" role="img" aria-label="Black-and-white photograph of a tattooed model's back with long dark hair"></div>
    <div class="brand-block">
      <div class="brand-name">Velvet Harbor</div>
      <div class="tagline">Strength, Elegance, and Beauty</div>
    </div>
  </section>

  <section class="card card-back">
    <div class="contact-block">
      <div class="person-name">Rolf Lindqvist</div>
      <div class="person-title">Photographer / Owner</div>
      <ul class="contact-list">
        <li><span class="label">P</span>(941) 555-0148</li>
        <li><span class="label">E</span>rolf@velvetharborphotoworks.com</li>
        <li><span class="label">W</span>www.velvetharborphotoworks.com</li>
        <li><span class="label">A</span>4630 Marlow Ave W Parrish, FL 34218</li>
      </ul>
    </div>
    <div class="brand-name">Velvet Harbor</div>
    <div class="ornament" role="img" aria-label="Faint decorative swirl ornament"></div>
  </section>
</body>
</html>
```